The Notebook Behind Every Turn - Book cover design

Book Cover Designer Task Description for a 170 page 6x9 white RVL book.
Title: The Notebook Behind Every Turn
Author: Mark Fulbrook
ISBN: 978-1-5318864-7-9
Concept (images are for examples only)
The cover should visually represent the protagonist’s transformation from corporate captivity in Sydney to freedom and reflection in Chiang Mai. The design should feel aspirational, modern, and professional, appealing to readers of personal development, lifestyle design, and narrative nonfiction.
Front Cover Visual Direction
• Left Scene (Sydney):
• A female figure, circa 40years old, in business attire leaving a high‑rise office building at dusk.
• She carries a large office travel bag or briefcase bag.
• The Sydney skyline should be visible in the background, with evening light (purples, oranges, city lights).
• Mood: heavy, corporate, restrained.
• Right Scene (Chiang Mai):
• The same woman, now relaxed, sitting at an outdoor café table in the sunshine.
• She has a coffee in hand, with her journal open on the table.
• Background hints of Chiang Mai: golden temple spire, tropical greenery, warm sunlight.
• Mood: light, free, expansive.
• Design Style:
• A split‑scene composition (left = Sydney evening, right = Chiang Mai morning).
• Title across the centre in bold, modern typography.
• Author name at the bottom.
Back Cover
• Blurb (to include in full):
What if the life you’re living isn’t yours at all?
You followed the rules, climbed the ladder, and earned the perks. But something still feels off. The Sunday dread. The quiet discontent. The whisper that says: This can’t be it.
The Notebook Behind Every Turn is a raw, reflective journey through corporate captivity, awakening, and the first steps toward freedom. Through the eyes of Helen, a high-performing professional caught in the illusion of security, this book explores what happens when you finally question everything you were told about success, stability, and self-worth.
Blending narrative storytelling with coaching prompts, global lifestyle insights, and real-world case studies, this book offers more than inspiration. It’s a blueprint for change. Whether you’re stuck in the “one more year” loop or quietly dreaming of a different life, this is your invitation to reclaim your time, energy, and direction.
Author Bio:
Mark Fulbrook is the author of The Storm Nobody Has Noticed, known for blending creative insight with operational clarity. His work explores the intersection of personal freedom, global mobility, and the systems that shape our choices. Through writing and coaching, he helps readers design lives that are intentional, resilient, and deeply their own.
• ISBN: 978-1-5318864-7-9
• Include barcode space at bottom right.

Target Market(s)

Bored workers between 20-50 looking for a way out of the rat race

Industry/Entity Type

Self help

Colors

Designer to choose colors to be used in the design.

Requirements
Must have
• A worn out woman in her thirties leaving a Sydney office on a grey evening in formal office attire and the same lady dressed casually and happy having a coffee in a café in Chiang Mai with her journal then the same woman
Nice to have
• Temple in the background and maybe a group of young people at other tables looking happy

```html
<!DOCTYPE html>
<html lang="en">
<head>
<meta charset="utf-8">
<title>The Notebook Behind Every Turn – Cover Wrap</title>
<link rel="stylesheet" href="https://fonts.googleapis.com/css2?family=Montserrat:wght@300;400;600;700;800&display=swap">
<style>
  :root{
    --back-top:#24166a;
    --back-bottom:#3e2b7a;
    --spine:#a967b2;
    --ink-light:#ffffff;
    --sydney-dark:#1d1a4f;
    --sydney-mid:#4a3b86;
    --sydney-dusk:#b86a8a;
    --mai-gold:#e7b25c;
    --mai-green:#5d7a3a;
    --mai-deep:#3c4f2a;
  }
  *{margin:0;padding:0;box-sizing:border-box}
  html,body{width:1200px;height:879px;overflow:hidden;background:#fff}
  .wrap{position:relative;width:1200px;height:879px;font-family:"Montserrat",sans-serif;color:var(--ink-light);text-transform:uppercase}

  /* Back cover */
  .back{position:absolute;left:0;top:0;width:582px;height:879px;background:linear-gradient(180deg,var(--back-top) 0%,var(--back-bottom) 100%)}
  .back-title{position:absolute;left:81px;top:106px;font-weight:700;font-size:17.5px;letter-spacing:.03em;white-space:nowrap}
  .rule{position:absolute;height:5px;background:var(--ink-light)}
  .rule-top{left:149px;top:139px;width:295px}
  .rule-bottom{left:147px;top:515px;width:296px}
  .blurb{position:absolute;left:101px;top:157px;width:395px;font-weight:600;font-size:12.4px;line-height:15.85px;letter-spacing:.02em}
  .author-photo{position:absolute;left:81px;top:549px;width:120px;height:128px;border:1.5px solid #fff;background:linear-gradient(135deg,#7a5a3a 0%,#c9a27a 45%,#3a4f8a 100%)}
  .bio{position:absolute;left:207px;top:540px;width:292px;font-weight:300;font-size:12.6px;line-height:15.85px;letter-spacing:.04em}
  .bio strong{font-weight:700}
  .barcode-space{position:absolute;left:363px;top:747px;width:180px;height:100px;background:#fff}

  /* Spine */
  .spine{position:absolute;left:582px;top:0;width:36px;height:879px;background:var(--spine)}
  .spine-text{position:absolute;left:9px;font-weight:300;font-size:18px;letter-spacing:.02em;writing-mode:vertical-rl;white-space:nowrap;line-height:18px}
  .spine-title{top:75px}
  .spine-author{top:582px}

  /* Front cover */
  .front{position:absolute;left:618px;top:0;width:582px;height:879px;overflow:hidden}
  .scene{position:absolute;top:0;height:879px}
  .scene-sydney{left:0;width:281px;background:linear-gradient(180deg,var(--sydney-dark) 0%,var(--sydney-mid) 38%,var(--sydney-dusk) 48%,var(--sydney-mid) 58%,var(--sydney-dark) 100%)}
  .scene-mai{left:281px;width:301px;background:linear-gradient(180deg,#6a4f8a 0%,var(--mai-gold) 30%,var(--mai-green) 65%,var(--mai-deep) 100%)}
  .front-title{position:absolute;left:103px;top:64px;width:362px;text-align:center;text-shadow:0 2px 6px rgba(0,0,0,.45)}
  .front-title span{display:block;line-height:1}
  .t-light{font-weight:300;font-size:36px;letter-spacing:.04em}
  .t-spaced{font-weight:300;font-size:28px;letter-spacing:.18em;margin:2px 0}
  .t-bold{font-weight:800;font-size:62px;letter-spacing:-.01em}
  .t-bold-sm{font-weight:800;font-size:54px;letter-spacing:0}
  .front-author{position:absolute;left:100px;top:794px;width:380px;text-align:center;font-weight:700;font-size:44px;white-space:nowrap;text-shadow:0 2px 6px rgba(0,0,0,.45)}
</style>
</head>
<body>
<div class="wrap">

  <section class="back">
    <h2 class="back-title">The Notebook Behind Every Turn</h2>
    <div class="rule rule-top"></div>
    <p class="blurb">What if the life you’re living isn’t yours at all? You followed the rules, climbed the ladder, and earned the perks. But something still feels off. The Sunday dread. The quiet discontent. The whisper that says: This can’t be it.<br>The Notebook Behind Every Turn is a raw, reflective journey through corporate captivity, awakening, and the first steps toward freedom. Through the eyes of Helen, a high-performing professional caught in the illusion of security, this book explores what happens when you finally question everything you were told about success, stability, and self-worth.<br>Blending narrative storytelling with coaching prompts, global lifestyle insights, and real-world case studies, this book offers more than inspiration. It’s a blueprint for change. Whether you’re stuck in the “one more year” loop or quietly dreaming of a different life, this is your invitation to reclaim your time, energy, and direction.</p>
    <div class="rule rule-bottom"></div>
    <div class="author-photo" role="img" aria-label="Author portrait photograph"></div>
    <p class="bio"><strong>Mark Fulbrook</strong> is the author of The Storm Nobody Has Noticed, known for blending creative insight with operational clarity. His work explores the intersection of personal freedom, global mobility, and the systems that shape our choices. Through writing and coaching, he helps readers design lives that are intentional, resilient, and deeply their own.</p>
    <div class="barcode-space"></div>
  </section>

  <section class="spine">
    <span class="spine-text spine-title">The Notebook Behind Every Turn</span>
    <span class="spine-text spine-author">Mark Fulbrook</span>
  </section>

  <section class="front">
    <div class="scene scene-sydney" role="img" aria-label="Illustration: a tired woman in business attire carrying a bag leaves an office building at dusk, Sydney skyline behind"></div>
    <div class="scene scene-mai" role="img" aria-label="Illustration: the same woman relaxed at a café table in Chiang Mai with coffee and an open journal, golden temple and greenery behind"></div>
    <h1 class="front-title">
      <span class="t-light">The</span>
      <span class="t-bold">Notebook</span>
      <span class="t-spaced">Behind</span>
      <span class="t-bold-sm">Every Turn</span>
    </h1>
    <div class="front-author">Mark Fulbrook</div>
  </section>

</div>
</body>
</html>
```